Webdesign für einen gemeinnützigen Verein
Zielgruppe
Merovalien e. V. ist ein gemeinnütziger Verein der sich auf die Fahne geschrieben hat sich für Inklusive und Vielfalt einzusetzen. Wir unterstützen Menschen mit Behinderung beim selbstbestimmten Leben und helfen auch bei Anträgen etc. Des weiteren helfen wir Firmen, Vereinen und stonstigen Organisationen Ihre Inhalte und Auftritte barrierefrei zu gestallten. Wir Testen Apps und Websites und geben hier Feedback.
Aufgabenstellung
Wir möchten ein WordPress Theme das responsiv und persistent ist. Wir möchten die Inhalte später mit WordPress Einpflege und die Seite managen.
Unser Corporate Design steht bereits und beinhaltet die Pride Farben und sollte somit in einem hellen und dunklen Design umgesetzt werden. Wir möchten hier 2 Varianten vom Homepage Design (Darkmode)
Poppins ist unsere Schriftart für Textinhalte
Google Fonds möchten wir nicht nutzen
Passende Social Media Icons

```html
<!DOCTYPE html>
<html lang="de">
<head>
<meta charset="utf-8">
<title>Merovalien e. V. – Homepage Entwurf</title>
<link rel="stylesheet" href="https://fonts.googleapis.com/css2?family=Poppins:wght@300;400;500;600;700&display=swap">
<style>
:root{
  --bg-top:#17183a;
  --bg-mid:#2a1645;
  --bg-bottom:#3c1a5e;
  --brand:#5a1b7c;
  --brand-dark:#431462;
  --brand-btn:#4a1769;
  --ink:#2b2b2b;
  --ink-soft:#555;
  --paper:#ffffff;
  --paper-gray:#e6e6e8;
  --nav-gray:#e1e1e3;
  --muted-lilac:#d9cfe4;
  --rainbow:linear-gradient(90deg,#e40303,#ff8c00,#ffed00,#008026,#004dff,#750787);
  --dark-panel:linear-gradient(180deg,#4b1670 0%,#2d1650 45%,#1b1b3c 100%);
}
*{box-sizing:border-box;margin:0;padding:0}
html,body{width:1200px;height:4227px;overflow:hidden}
body{font-family:"Poppins",sans-serif;color:var(--ink);
  background:linear-gradient(160deg,var(--bg-top) 0%,var(--bg-mid) 55%,var(--bg-bottom) 100%)}
.board{position:relative;width:1200px;height:4227px}
.abs{position:absolute}
.screen{position:absolute;overflow:hidden}
.white{background:var(--paper)}
.gray{background:var(--paper-gray)}
.dark{background:var(--dark-panel);color:#fff}

/* brand */
.brand{display:flex;align-items:center;gap:6px;font-weight:600;color:var(--brand);letter-spacing:.02em}
.brand-dot{border-radius:50%;background:var(--brand);flex:none}
.rainbow-line{height:4px;border-radius:2px;background:var(--rainbow)}

/* nav */
.nav{position:absolute;left:0;right:0;height:59px;background:var(--nav-gray);display:flex;align-items:center;padding:0 0 0 48px}
.nav .brand{font-size:12px;color:#333;font-weight:500}
.nav .brand-dot{width:26px;height:26px}
.menu{position:absolute;top:0;height:59px;display:flex;align-items:center;font-size:10.5px;color:#333}
.menu span{position:absolute;white-space:nowrap}
.menu .home{background:var(--rainbow);color:#fff;padding:1px 8px;border-radius:8px;font-size:9.5px}
.mode-toggle{position:absolute;top:20px;width:39px;height:20px;border-radius:10px;background:#fff;border:1px solid #ccc}
.mode-toggle::before{content:"";position:absolute;left:4px;top:3px;width:12px;height:12px;border-radius:50%;background:var(--brand-dark)}
.mode-toggle::after{content:"";position:absolute;right:7px;top:5px;width:8px;height:8px;border-radius:50%;background:#222}

/* buttons */
.btn{position:absolute;background:var(--brand-btn);color:#fff;font-weight:600;border-radius:8px;text-transform:uppercase;letter-spacing:.04em;display:flex;align-items:center;justify-content:center;box-shadow:0 2px 4px rgba(0,0,0,.25)}
.up{position:absolute;border-radius:50%;border:2px solid var(--brand-dark);display:flex;align-items:center;justify-content:center}
.socials{position:absolute;display:flex}
.socials i{display:block;border-radius:50%;border:2px solid var(--brand-dark);background:#fff}

.section-title{position:absolute;left:0;right:0;text-align:center;font-weight:600;color:#222;text-transform:uppercase}
.hero-lead{position:absolute;color:#333;font-weight:400}
.hero-lead b{color:var(--brand);font-weight:700}
.typed{font-weight:700;color:var(--brand);letter-spacing:.03em}
.quote-mark{position:absolute;font-family:Georgia,serif;font-weight:700;color:var(--muted-lilac);line-height:1}
.slider-arrow{position:absolute;color:#bbb}

.body-copy{position:absolute;color:#333}
.body-copy b{color:var(--brand);font-weight:600}
.photo{position:absolute;border-radius:4px}
.photo-office{background:linear-gradient(135deg,#c9ccd3,#6d7280 60%,#3b3f48)}
.illustration{background:radial-gradient(ellipse at 55% 55%,#d4c7f3 0%,#b6a2ec 45%,rgba(230,230,232,0) 72%)}
.portrait{border-radius:10px;background:linear-gradient(180deg,#8a8a90,#3e3e44);display:flex;align-items:center;justify-content:center;color:rgba(255,255,255,.85)}
.person-name{position:absolute;text-align:center;font-weight:700;color:#222;text-transform:uppercase}
.person-role{position:absolute;text-align:center;font-weight:600;color:var(--brand);text-transform:uppercase}
.team-banner{position:absolute;border-radius:8px;background:linear-gradient(90deg,#6a3a8f,#7c4fa2 50%,#5b2f7f);color:#fff;text-align:center;display:flex;flex-direction:column;justify-content:center}

.dark-title{position:absolute;left:0;right:0;text-align:center;font-weight:700;color:#fff;text-transform:uppercase}
.dark-copy{position:absolute;left:0;right:0;text-align:center;color:#eee}
.partner{position:absolute;height:16px;border-radius:8px;background:rgba(255,255,255,.22)}
.map{position:absolute;border-radius:12px;background:linear-gradient(135deg,#f4f2ee,#e8e6e1 60%,#dedcd6)}
.foot-text{position:absolute;color:#ddd;line-height:1.55}
.foot-brand{position:absolute;font-weight:700;color:#e7a3ff;letter-spacing:.03em}
.email-field{position:absolute;border-radius:4px;background:#c9c9d3;color:#666;padding-left:6px}
.newsletter{color:#7c84ff}
.copyright-bar{position:absolute;background:var(--rainbow);color:#fff;text-align:center}
.copyright-bar b{font-weight:700}
</style>
</head>
<body>
<div class="board">

<!-- ============ MOBILE ============ -->
<!-- splash -->
<section class="screen white" style="left:43px;top:44px;width:259px;height:460px">
  <div class="brand abs" style="left:84px;top:212px;font-size:13px"><span class="brand-dot" style="width:16px;height:16px"></span>MEROVALIEN</div>
  <div class="rainbow-line abs" style="left:57px;top:281px;width:144px"></div>
</section>

<!-- hero -->
<section class="screen white" style="left:43px;top:504px;width:259px;height:461px">
  <div class="nav" style="padding-left:15px;height:62px;background:var(--nav-gray)">
    <div class="brand"><span class="brand-dot" style="width:24px;height:24px"></span><span style="font-size:9.5px">MEROVALIEN</span></div>
    <span class="abs" style="left:222px;top:23px;width:20px;height:17px;border-radius:4px;background:var(--rainbow)"></span>
  </div>
  <div class="socials" style="left:62px;top:88px;gap:17px"><i style="width:13px;height:13px"></i><i style="width:13px;height:13px"></i><i style="width:13px;height:13px"></i><i style="width:13px;height:13px"></i><i style="width:13px;height:13px"></i></div>
  <div class="abs" style="left:15px;top:165px;width:230px;height:120px;border-radius:50%;background:rgba(0,0,0,.03)"></div>
  <div class="hero-lead" style="left:0;right:0;top:128px;text-align:center;font-size:15px;line-height:1.78">
    <span class="typed" style="font-size:16px">MEROVALI</span><br>Verein zur Förderung<br>der <b>Kommunikation</b><br>und <b>Inklusion</b> für ein<br>selbstbestimmtes<br>Leben e. V.
  </div>
  <div class="btn" style="left:82px;top:300px;width:88px;height:24px;font-size:7px">Mehr erfahren</div>
  <div class="quote-mark" style="left:24px;top:330px;font-size:34px">“</div>
  <div class="abs" style="left:20px;right:20px;top:356px;text-align:center;font-size:9px;line-height:1.8;color:#333">Sprache ist der Schlüssel zur Inklusion :<br>Merovalien öffnet Türen</div>
  <div class="quote-mark" style="left:204px;top:378px;font-size:34px">”</div>
  <div class="slider-arrow" style="left:91px;top:423px;font-size:16px">‹</div>
  <div class="slider-arrow" style="left:155px;top:423px;font-size:16px">›</div>
</section>

<!-- was macht uns aus -->
<section class="screen gray" style="left:43px;top:965px;width:259px;height:460px">
  <div class="section-title" style="top:20px;font-size:14px;color:var(--brand-dark)">Was macht uns aus?</div>
  <div class="photo illustration" role="img" aria-label="Illustration: Gruppe von Menschen, eine Person im Rollstuhl, mit Pflanzen" style="left:47px;top:45px;width:156px;height:87px"></div>
  <div class="body-copy" style="left:28px;top:143px;width:192px;font-size:7.2px;line-height:1.38">
    <b>Merovalien</b> beschäftigt sich mit der Förderung von selbstbestimmtem Leben von Menschen mit Behinderungen sowie der Schaffung von Barrierefreiheit bei digitalen Medien.<br>Ein weiterer Fokus liegt auf der Verbesserung der Kommunikation zwischen Menschen, Institutionen und Organisationen, insbesondere zwischen Menschen mit und ohne Behinderungen.<br>Ziel ist es, Barrieren zu beseitigen und eine inklusive Gesellschaft zu schaffen, in der alle Menschen gleichermaßen teilhaben können. Die Förderung von Empowerment und die Stärkung der Stimmen von Menschen mit Behinderungen sind ebenfalls wichtige Bestandteile von Merovalien. gen voranzutreiben. Durch die Förderung einer offenen und vielfältigen Kommunikation, die Schaffung von barrierefreien Angeboten und die Verbreitung von Wissen und Informationen über Behinderungen und Inklusion kann eine inklusive Gesellschaft erreicht werden, in der jeder Mensch gleichberechtigt und selbstbestimmt leben kann.
  </div>
  <div class="btn" style="left:90px;top:408px;width:72px;height:20px;font-size:6px">Mehr erfahren</div>
</section>

<!-- was machen wir -->
<section class="screen white" style="left:43px;top:1425px;width:259px;height:463px">
  <div class="section-title" style="top:10px;font-size:14px">Was machen wir?</div>
  <div class="photo photo-office" role="img" aria-label="Foto: Podcast-Aufnahme mit mehreren Personen" style="left:54px;top:30px;width:151px;height:96px"></div>
  <div class="body-copy" style="left:18px;top:134px;width:222px;font-size:7px;line-height:1.4;text-align:center">Unsere zahlreichen Podcast behandeln die Themen wofür wir stehen was uns ausmacht. Wir möchten über dieses Medium mit Sprache zeigen wie wichtig die Kommunikation ist. Wir wollen aufklären und Wissen vermitteln. Ob zu gesellschaftlichen Themen im Bereich der Inklusion oder Barrierefreiheit in digitalen Medien. Egal ob Techik wie SmartHome oder Gaming.</div>
  <div class="btn" style="left:92px;top:203px;width:72px;height:18px;font-size:6px">Mehr erfahren</div>
  <div class="photo photo-office" role="img" aria-label="Foto: Vortrag in einem Besprechungsraum" style="left:54px;top:233px;width:151px;height:99px"></div>
  <div class="body-copy" style="left:15px;top:337px;width:228px;font-size:7px;line-height:1.45;text-align:justify"><strong>Vortrag und Kommunikationsprojekt zum Persönlichen Budget</strong> Assistenz für Menschen mit Behinderungen ist wichtig um ein selbstbestimmtes Leben zu gestalten. Dieser Vortrag führte im Anschluss zu einer Community über die sich Betroffene und Beratende Personen austauschen. Höre jetzt den Vortrag und trete der Community bei.<br><span style="color:var(--brand)">... mehr erfahren unterseite zu den Infos und Vortrag Communityetc.</span></div>
  <div class="btn" style="left:128px;top:425px;width:100px;height:22px;font-size:7px">Weitere Projekte</div>
</section>

<!-- wer sind wir -->
<section class="screen gray" style="left:43px;top:1888px;width:259px;height:460px">
  <div class="team-banner" role="img" aria-label="Bannerfoto mit Teammitgliedern" style="left:16px;top:18px;width:227px;height:44px">
    <div style="font-size:12px;font-weight:600">WER SIND WIR?</div>
    <div style="font-size:8px">“Gemeinsam aktiv für eine inklusive Zukunft”</div>
  </div>
  <div class="photo portrait" role="img" aria-label="Porträtfoto Deniz Kartal" style="left:49px;top:128px;width:161px;height:212px;font-size:13px">siehe Profil</div>
  <div class="person-name" style="left:0;right:0;top:356px;font-size:14px">Deniz Kartal</div>
  <div class="person-role" style="left:0;right:0;top:378px;font-size:14px">Vorstand</div>
</section>
<section class="screen white" style="left:43px;top:2348px;width:259px;height:462px">
  <div class="photo portrait" role="img" aria-label="Porträtfoto Miriam Vogt" style="left:49px;top:98px;width:161px;height:213px;font-size:13px">siehe Profil</div>
  <div class="person-name" style="left:0;right:0;top:326px;font-size:14px">Miriam Vogt</div>
  <div class="person-role" style="left:0;right:0;top:348px;font-size:14px">Vorstand</div>
</section>
<section class="screen gray" style="left:43px;top:2810px;width:259px;height:457px">
  <div class="photo portrait" role="img" aria-label="Porträtfoto Lukas Brenner" style="left:49px;top:97px;width:161px;height:212px;font-size:13px">siehe Profil</div>
  <div class="person-name" style="left:0;right:0;top:325px;font-size:14px">Lukas Brenner</div>
  <div class="person-role" style="left:0;right:0;top:346px;font-size:14px">Vorstand</div>
</section>

<!-- mobile dark footer -->
<section class="screen dark" style="left:43px;top:3267px;width:259px;height:927px">
  <div class="dark-title" style="top:27px;font-size:14px">Mit dir ein größeres Wir</div>
  <div class="dark-copy" style="top:58px;padding:0 22px;font-size:6.3px;line-height:1.5">Willst du dich für eine inklusive und barrierefreie Gesellschaft einsetzen und Menschen mit Behinderungen dabei helfen, ein selbstbestimmtes Leben zu führen? Dann bist du bei unserem Verein Merovalien e. V. genau richtig! Gemeinsam möchten wir Barrieren abbauen, Vorurteile überwinden und eine vielfältige und offene Kommunikation fördern. Wir suchen motivierte Menschen, die sich für eine bessere Welt einsetzen möchten und aktiv etwas bewirken wollen. Werde Teil unserer Community und trage dazu bei, dass Inklusion und Barrierefreiheit in unserer Gesellschaft gelebt werden! Melde dich jetzt bei uns und werde Teil unserer Bewegung!</div>
  <div class="btn" style="left:93px;top:200px;width:72px;height:17px;font-size:6px">Mehr erfahren</div>
  <div class="partner" style="left:16px;top:252px;width:86px"></div><div class="partner" style="left:129px;top:252px;width:114px"></div>
  <div class="partner" style="left:16px;top:283px;width:86px"></div><div class="partner" style="left:142px;top:283px;width:82px"></div>
  <div class="partner" style="left:16px;top:316px;width:86px"></div><div class="partner" style="left:142px;top:316px;width:90px"></div>
  <div class="map" role="img" aria-label="Stadtplan mit Standort des Vereins" style="left:16px;top:361px;width:227px;height:79px;border-radius:6px"></div>
  <div class="foot-brand" style="left:47px;top:502px;font-size:17px">MEROVALIEN</div>
  <div class="foot-text" style="left:47px;top:528px;width:180px;font-size:7.5px;line-height:1.25;text-align:center">—— Verein zur Förderung der ——<br>Kommunikation und Inklusion<br>für ein selbstbestimmtes Leben e.V.</div>
  <div class="foot-text" style="left:47px;top:575px;font-size:9px;line-height:1.95">
    Merovalien e. V.<br>c/o Brenner Lindauer Str. 14<br>10781 Berlin<br>Tel.&nbsp;&nbsp;&nbsp;&nbsp;: +49 (0) 30 5518 4420<br>Fax.&nbsp;&nbsp;&nbsp;: +49 (0) 30 5518 4421<br>E-Mail : info@merovalien.de<br>Service<br>Blog<br>Privacy &amp; Policy<br>Sitemap<br>Barrierefreiheit
  </div>
  <div class="email-field" style="left:47px;top:789px;width:143px;height:14px;font-size:7px">email</div>
  <div class="foot-text" style="left:47px;top:806px;font-size:9px;line-height:1.95"><span class="newsletter">Abonnieren Sie unseren Newsletter</span><br>Impressum<br>Datenschutzerklärung<br>Cookie-Richtlinie</div>
  <div class="copyright-bar" style="left:0;right:0;top:903px;height:21px;font-size:7px;line-height:21px">© 2023, <b>MEROVALIEN</b> All rights reserved</div>
</section>

<!-- ============ DESKTOP ============ -->
<!-- splash -->
<section class="screen white" style="left:338px;top:44px;width:819px;height:460px">
  <div class="brand abs" style="left:383px;top:213px;font-size:14px"><span class="brand-dot" style="width:18px;height:18px"></span>MEROVALIEN</div>
  <div class="rainbow-line abs" style="left:339px;top:281px;width:142px"></div>
</section>

<!-- hero -->
<section class="screen white" style="left:338px;top:504px;width:819px;height:461px">
  <div class="nav" style="top:0">
    <div class="brand"><span class="brand-dot"></span>MEROVALIEN</div>
    <div class="menu" style="left:0;right:0"><span class="home" style="left:296px">Home</span><span style="left:378px">Verein</span><span style="left:419px">Projekte</span><span style="left:488px">Team</span><span style="left:542px">Blog</span><span style="left:586px">Wir im Netz</span><span style="left:658px">Kontakt</span></div>
    <div class="mode-toggle" style="left:729px"></div>
  </div>
  <div class="socials" style="left:636px;top:78px;gap:17px"><i style="width:13px;height:13px"></i><i style="width:13px;height:13px"></i><i style="width:13px;height:13px"></i><i style="width:13px;height:13px"></i><i style="width:13px;height:13px"></i></div>
  <div class="abs" style="left:503px;top:120px;width:250px;height:230px;border-radius:50%;background:radial-gradient(circle,#f4f4f6,#fff 70%)"></div>
  <div class="hero-lead" style="left:110px;top:152px;font-size:20px;line-height:1.55">
    <span class="typed" style="font-size:20px">MEROVA</span>|<br>Verein zur Förderung der<br><b>Kommunikation</b> und <b>Inklusion</b><br>für ein selbstbestimmtes Leben e. V.
  </div>
  <div class="btn" style="left:110px;top:289px;width:89px;height:26px;font-size:7.5px">Mehr erfahren</div>
  <div class="quote-mark" style="left:108px;top:336px;font-size:72px">“</div>
  <div class="abs" style="left:153px;top:384px;font-size:15px;color:#333">Sprache ist der Schlüssel zur Inklusion : Merovalien öffnet Türen</div>
  <div class="quote-mark" style="left:660px;top:400px;font-size:72px">”</div>
  <div class="slider-arrow" style="left:46px;top:216px;font-size:24px">‹</div>
  <div class="slider-arrow" style="left:759px;top:216px;font-size:24px">›</div>
</section>

<!-- was macht uns aus -->
<section class="screen gray" style="left:338px;top:965px;width:819px;height:460px">
  <div class="nav" style="top:0">
    <div class="brand"><span class="brand-dot"></span>MEROVALIEN</div>
    <div class="menu" style="left:0;right:0"><span class="home" style="left:296px">Home</span><span style="left:378px">Verein</span><span style="left:419px">Projekte</span><span style="left:488px">Team</span><span style="left:542px">Blog</span><span style="left:586px">Wir im Netz</span><span style="left:658px">Kontakt</span></div>
    <div class="mode-toggle" style="left:729px"></div>
  </div>
  <div class="section-title" style="top:80px;font-size:21px">Was macht uns aus?</div>
  <div class="body-copy" style="left:110px;top:123px;width:316px;font-size:10px;line-height:1.48">
    <b>Merovalien</b> beschäftigt sich mit der Förderung von selbstbestimmtem Leben von Menschen mit Behinderungen sowie der Schaffung von Barrierefreiheit bei digitalen Medien.<br>Ein weiterer Fokus liegt auf der Verbesserung der Kommunikation zwischen Menschen, Institutionen und Organisationen, insbesondere zwischen Menschen mit und ohne Behinderungen.<br>Ziel ist es, Barrieren zu beseitigen und eine inklusive Gesellschaft zu schaffen, in der alle Menschen gleichermaßen teilhaben können.<br>Die Förderung von Empowerment und die Stärkung der Stimmen von Menschen mit Behinderungen sind ebenfalls wichtige Bestandteile von Merovalien.<br>gen voranzutreiben. Durch die Förderung einer offenen und vielfältigen Kommunikation, die Schaffung von barrierefreien Angeboten und die Verbreitung von Wissen und Informationen über Behinderungen und Inklusion kann eine inklusive Gesellschaft erreicht werden, in der jeder Mensch gleichberechtigt und selbstbestimmt leben kann.
  </div>
  <div class="photo illustration" role="img" aria-label="Illustration: Gruppe von Menschen, eine Person im Rollstuhl, mit Pflanzen" style="left:433px;top:140px;width:312px;height:160px"></div>
  <div class="btn" style="left:550px;top:374px;width:90px;height:24px;font-size:7.5px">Mehr erfahren</div>
  <div class="up" style="left:727px;top:418px;width:22px;height:22px"><svg width="12" height="12" viewBox="0 0 12 12"><path d="M6 10V2M2 6l4-4 4 4" fill="none" stroke="#431462" stroke-width="1.8"/></svg></div>
</section>

<!-- was machen wir -->
<section class="screen white" style="left:338px;top:1425px;width:819px;height:463px">
  <div class="nav" style="top:0">
    <div class="brand"><span class="brand-dot"></span>MEROVALIEN</div>
    <div class="menu" style="left:0;right:0"><span class="home" style="left:296px">Home</span><span style="left:378px">Verein</span><span style="left:419px">Projekte</span><span style="left:488px">Team</span><span style="left:542px">Blog</span><span style="left:586px">Wir im Netz</span><span style="left:658px">Kontakt</span></div>
    <div class="mode-toggle" style="left:729px"></div>
  </div>
  <div class="section-title" style="top:80px;font-size:21px">Was machen wir?</div>
  <div class="photo photo-office" role="img" aria-label="Foto: Podcast-Aufnahme mit mehreren Personen" style="left:92px;top:135px;width:158px;height:105px"></div>
  <div class="body-copy" style="left:296px;top:132px;width:474px;font-size:9.5px;line-height:1.8;text-align:justify">Unsere zahlreichen Podcast behandeln die Themen wofür wir stehen was uns ausmacht. Wir möchten über dieses Medium mit Sprache zeigen wie wichtig die Kommunikation ist. Wir wollen aufklären und Wissen vermitteln. Ob zu gesellschaftlichen Themen im Bereich der Inklusion oder Barrierefreiheit in digitalen Medien. Egal ob Techik wie SmartHome oder Gaming.</div>
  <div class="btn" style="left:296px;top:214px;width:88px;height:24px;font-size:7.5px">Mehr erfahren</div>
  <div class="photo photo-office" role="img" aria-label="Foto: Vortrag in einem Besprechungsraum" style="left:92px;top:271px;width:158px;height:105px"></div>
  <div class="body-copy" style="left:296px;top:268px;width:474px;font-size:9.5px;line-height:1.8;text-align:justify"><strong style="font-size:10.5px">Vortrag und Kommunikationsprojekt zum Persönlichen Budget</strong><br>Assistenz für Menschen mit Behinderungen ist wichtig um ein selbstbestimmtes Leben zu gestalten. Dieser Vortrag führte im Anschluss zu einer Community über die sich Betroffene und Beratende Personen austauschen. Höre jetzt den Vortrag und trete der Community bei.</div>
  <div class="body-copy" style="left:296px;top:351px;font-size:9.5px;color:var(--brand)">... mehr erfahren unterseite zu den Infos und Vortrag Community etc.</div>
  <div class="btn" style="left:358px;top:398px;width:104px;height:26px;font-size:7.5px">Weitere Projekte</div>
  <div class="up" style="left:727px;top:421px;width:22px;height:22px"><svg width="12" height="12" viewBox="0 0 12 12"><path d="M6 10V2M2 6l4-4 4 4" fill="none" stroke="#431462" stroke-width="1.8"/></svg></div>
</section>

<!-- wer sind wir -->
<section class="screen gray" style="left:338px;top:1888px;width:819px;height:460px">
  <div class="nav" style="top:0">
    <div class="brand"><span class="brand-dot"></span>MEROVALIEN</div>
    <div class="menu" style="left:0;right:0"><span class="home" style="left:296px">Home</span><span style="left:378px">Verein</span><span style="left:419px">Projekte</span><span style="left:488px">Team</span><span style="left:542px">Blog</span><span style="left:586px">Wir im Netz</span><span style="left:658px">Kontakt</span></div>
    <div class="mode-toggle" style="left:729px"></div>
  </div>
  <div class="team-banner" role="img" aria-label="Bannerfoto mit Teammitgliedern" style="left:154px;top:67px;width:509px;height:100px">
    <div style="font-size:21px;font-weight:600">WER SIND WIR?</div>
    <div style="font-size:19px;letter-spacing:.03em">“Gemeinsam aktiv für eine inklusive Zukunft”</div>
  </div>
  <div class="photo portrait" role="img" aria-label="Porträtfoto Deniz Kartal" style="left:154px;top:225px;width:106px;height:136px;font-size:10px">siehe Profil</div>
  <div class="person-name" style="left:132px;width:150px;top:372px;font-size:9.5px">Deniz Kartal</div>
  <div class="person-role" style="left:132px;width:150px;top:386px;font-size:9.5px;color:#222">Vorstand</div>
  <div class="photo portrait" role="img" aria-label="Porträtfoto Miriam Vogt" style="left:356px;top:225px;width:106px;height:136px;font-size:10px">siehe Profil</div>
  <div class="person-name" style="left:334px;width:150px;top:372px;font-size:9.5px">Miriam Vogt</div>
  <div class="person-role" style="left:334px;width:150px;top:386px;font-size:9.5px;color:#222">Vorstand</div>
  <div class="photo portrait" role="img" aria-label="Porträtfoto Lukas Brenner" style="left:560px;top:225px;width:106px;height:136px;font-size:10px">siehe Profil</div>
  <div class="person-name" style="left:538px;width:150px;top:372px;font-size:9.5px">Lukas Brenner</div>
  <div class="person-role" style="left:538px;width:150px;top:386px;font-size:9.5px;color:#222">Vorstand</div>
  <div class="up" style="left:727px;top:419px;width:22px;height:22px"><svg width="12" height="12" viewBox="0 0 12 12"><path d="M6 10V2M2 6l4-4 4 4" fill="none" stroke="#431462" stroke-width="1.8"/></svg></div>
</section>

<!-- desktop dark footer -->
<section class="screen dark" style="left:338px;top:2348px;width:819px;height:718px">
  <div class="dark-title" style="top:22px;font-size:21px;letter-spacing:.02em">Mit dir ein größeres Wir</div>
  <div class="dark-copy" style="top:64px;padding:0 80px;font-size:10px;line-height:1.56">Willst du dich für eine inklusive und barrierefreie Gesellschaft einsetzen und<br>Menschen mit Behinderungen dabei helfen, ein selbstbestimmtes Leben zu führen?<br>Dann bist du bei unserem Verein Merovalien e. V. genau richtig! Gemeinsam möchten wir Barrieren abbauen,<br>Vorurteile überwinden und eine vielfältige und offene Kommunikation fördern.<br>Wir suchen motivierte Menschen, die sich für eine bessere Welt einsetzen möchten und aktiv etwas bewirken wollen.<br>Werde Teil unserer Community und trage dazu bei, dass Inklusion und Barrierefreiheit in unserer Gesellschaft gelebt werden!<br>Melde dich jetzt bei uns und werde Teil unserer Bewegung!</div>
  <div class="btn" style="left:365px;top:190px;width:88px;height:22px;font-size:7.5px">Mehr erfahren</div>
  <div class="partner" style="left:50px;top:259px;width:92px"></div>
  <div class="partner" style="left:172px;top:259px;width:122px"></div>
  <div class="partner" style="left:318px;top:259px;width:92px"></div>
  <div class="partner" style="left:448px;top:259px;width:82px"></div>
  <div class="partner" style="left:566px;top:259px;width:80px"></div>
  <div class="partner" style="left:682px;top:259px;width:88px"></div>
  <div class="map" role="img" aria-label="Stadtplan mit Standort des Vereins" style="left:49px;top:311px;width:721px;height:191px"></div>
  <div class="foot-brand" style="left:49px;top:530px;font-size:17px">MEROVALIEN</div>
  <div class="foot-text" style="left:49px;top:566px;font-size:9.5px;line-height:1.85">
    Merovalien e. V.<br>c/o Brenner Lindauer Str. 14<br>10781 Berlin<br>Tel.&nbsp;&nbsp;&nbsp;&nbsp;&nbsp;&nbsp;: +49 (0) 30 5518 4420<br>Fax.&nbsp;&nbsp;&nbsp;&nbsp;&nbsp;: +49 (0) 30 5518 4421<br>E-Mail : info@merovalien.de
  </div>
  <div class="foot-text" style="left:356px;top:584px;font-size:9.5px;line-height:1.85">Service<br>Blog<br>Privacy &amp; Policy<br>Sitemap<br>Barrierefreiheit</div>
  <div class="foot-text" style="left:585px;top:529px;width:186px;font-size:8.5px;line-height:1.2;text-align:right">—— Verein zur Förderung der ——<br>Kommunikation und Inklusion<br>für ein selbstbestimmtes Leben e. V.</div>
  <div class="email-field" style="left:585px;top:579px;width:141px;height:14px;font-size:7px">email</div>
  <div class="foot-text" style="left:585px;top:598px;font-size:9.5px;line-height:1.85"><span class="newsletter">Abonnieren Sie unseren Newsletter</span><br>Impressum<br>Datenschutzerklärung<br>Cookie-Richtlinie</div>
  <div class="up" style="left:727px;top:660px;width:22px;height:22px;border-color:#fff"><svg width="12" height="12" viewBox="0 0 12 12"><path d="M6 10V2M2 6l4-4 4 4" fill="none" stroke="#fff" stroke-width="1.8"/></svg></div>
  <div class="copyright-bar" style="left:0;right:0;top:697px;height:21px;font-size:8px;line-height:21px">© 2023, <b>MEROVALIEN</b> All rights reserved</div>
</section>

</div>
</body>
</html>
```